Contemporary new French wine brand needs logo and series of label design

to design a new contemporary logo and series of labels for a new French wine brand. We hope to attract not just current French wine drinkers but new ones who may appreciate a less traditional and more modern style.
Updates

Reason: we are wanting to extend the project for a few days more to receive more submissions since we had fewer designs submitted than we were expecting, maybe because of the holidays.

Target Market(s)

people who follow the arts community (eg. music, theatre, visual/video arts, dance) --- all mature ages.

Industry/Entity Type

French Wine

Requirements
Must have
• a clear, memorable treatment for the name CLAVINE with accompanying logo.
Nice to have
• embossing, matte/gloss refinement, tasteful foil stamping, coated stock for the whites to help the integrity of the paper in and out of ice buckets. A combo of say, three types of fonts; a semi custom font for the brand name Clavine and maybe a script and one other.
Should not have
• not traditional French

```html
<!DOCTYPE html>
<html lang="fr">
<head>
<meta charset="utf-8">
<title>Clavine – Val de Loire Sauvignon Blanc label</title>
<link rel="stylesheet" href="https://fonts.googleapis.com/css2?family=Cinzel:wght@400;600&family=Italianno&display=swap">
<style>
  :root {
    --backdrop: #e6e6e4;
    --stock: #f4f2e2;
    --stock-shade: #dcdbd0;
    --ink: #1c1a17;
    --foil: #b8952f;
    --foil-light: #e0c56a;
    --foil-deep: #8f6f1c;
  }
  * { margin: 0; padding: 0; box-sizing: border-box; }
  html, body {
    width: 748px;
    height: 1200px;
    overflow: hidden;
    background: var(--backdrop);
  }
  .canvas {
    position: relative;
    width: 748px;
    height: 1200px;
  }
  .label {
    position: absolute;
    left: 64px;
    top: 313px;
    width: 620px;
    height: 573px;
    background: linear-gradient(90deg, var(--stock) 0%, var(--stock) 45%, var(--stock-shade) 100%);
  }
  .vintage {
    position: absolute;
    left: 526px;
    top: 14px;
    font-family: "Cinzel", serif;
    font-size: 24px;
    letter-spacing: 3px;
    color: var(--foil);
    writing-mode: vertical-rl;
  }
  .foil-artwork {
    position: absolute;
    left: 79px;
    top: 91px;
    width: 462px;
    height: 218px;
    background: radial-gradient(ellipse at 50% 55%, var(--foil-light) 0%, var(--foil) 40%, rgba(184,149,47,0) 72%);
    opacity: 0.8;
  }
  .text-column {
    position: absolute;
    left: 0;
    top: 0;
    width: 604px;
    height: 100%;
  }
  .brand {
    position: absolute;
    left: 0;
    right: 0;
    top: 360px;
    text-align: center;
    font-family: "Cinzel", serif;
    font-weight: 600;
    font-size: 60px;
    line-height: 76px;
    letter-spacing: 4px;
    color: var(--ink);
  }
  .brand-rule {
    position: absolute;
    left: 157px;
    top: 437px;
    width: 293px;
    height: 2px;
    background: var(--ink);
  }
  .appellation {
    position: absolute;
    left: 0;
    right: 0;
    top: 470px;
    text-align: center;
    font-family: "Italianno", cursive;
    font-size: 46px;
    line-height: 46px;
    color: var(--foil);
  }
  .varietal {
    position: absolute;
    left: 0;
    right: 0;
    top: 521px;
    text-align: center;
    font-family: "Cinzel", serif;
    font-size: 22px;
    line-height: 26px;
    letter-spacing: 4px;
    color: var(--foil-deep);
  }
</style>
</head>
<body>
  <main class="canvas">
    <section class="label">
      <div class="vintage">2009</div>
      <div class="foil-artwork" role="img" aria-label="Gold foil brushwork artwork"></div>
      <div class="text-column">
        <h1 class="brand">Clavine</h1>
        <div class="brand-rule"></div>
        <p class="appellation">Val de Loire</p>
        <p class="varietal">Sauvignon Blanc</p>
      </div>
    </section>
  </main>
</body>
</html>
```